Playing Card Design for Magician's Business Card

Hello! I am looking for a two-sided design for a business card.
The back of the card look like the back of a playing card and includes the following text:
Desmond Halloway
www.TrickvaleShows.com
BACK:
Please - focus most of your time and effort on the BACK DESIGN.
Make it look like a playing card.
I plan to use this design to print up custom playing cards that I use in my show and give away to guests.
No Bunnies No Top Hats!
Not for kids. This is for sophisticated sleight of hand performed for adults.
Mood: Slick, elegant + fun.
See the attached samples of cards I like.
FRONT:
Not much text required ... Please leave plenty of blank space - minimalist.
The front of the card will have
First Name
Website
Phone Number
Email Address
Target Market(s)
Event Planners
Targeting corporate special events and private parties.
Industry/Entity Type
Magician
Contact Information for Business Card
Desmond Halloway
Illusionist
www.TrickvaleShows.com
Colors
Designer to choose colors to be used in the design.
Requirements
Must have
- Back must look like a playing card back.
- BACK MUST INCLUDE the following text:
- Desmond Halloway
- www.TrickvaleShows.com
Nice to have
- Symmetrical Design for back so the card looks the same if upside down.
- Please see "All Seeing Eye" design attached. Remove the Latin phrase and replace with Desmond (top left) Halloway (top right)
- TrickvaleShows.com (Lower middle)
Should not have
- Bunny Rabbits
- Top Hats
- Kids ....

```html
<!DOCTYPE html>
<html lang="en">
<head>
<meta charset="utf-8">
<title>Desmond Halloway – Playing Card Business Card</title>
<link rel="stylesheet" href="https://fonts.googleapis.com/css2?family=Almendra:wght@400;700&display=swap">
<style>
  :root {
    --backdrop: #9b9b9b;
    --card-black: #000000;
    --card-red: #d40a0c;
    --ornament-red: #a3080a;
    --ornament-deep: #5e0405;
  }
  html, body {
    margin: 0;
    padding: 0;
    width: 1200px;
    height: 900px;
    overflow: hidden;
    background: var(--backdrop);
  }
  .canvas {
    position: relative;
    width: 1200px;
    height: 900px;
  }
  .card {
    position: absolute;
    top: 214px;
    width: 270px;
    height: 474px;
    border-radius: 18px;
    overflow: hidden;
    background: var(--card-black);
  }
  .card--pattern { left: 288px; }
  .card--identity { left: 641px; }
  .card svg { display: block; width: 270px; height: 474px; }
  .frame-line { fill: var(--card-red); }
  .corner-arc { fill: var(--card-black); stroke: var(--card-red); stroke-width: 14; }
  .corner-ring { fill: none; stroke: var(--card-red); stroke-width: 8; }
  .corner-emblem { fill: var(--ornament-red); }
  .ornament-fill { fill: url(#ornamentTone); }
  .ornament-solid { fill: var(--ornament-red); }
  .card-name {
    font-family: "Almendra", serif;
    font-weight: 700;
    font-size: 44px;
    fill: var(--card-red);
  }
  .card-site {
    font-family: "Almendra", serif;
    font-weight: 700;
    font-size: 22px;
    fill: var(--card-red);
  }
</style>
</head>
<body>
<div class="canvas">

  <!-- Patterned side -->
  <div class="card card--pattern">
    <svg viewBox="0 0 450 790" xmlns="http://www.w3.org/2000/svg">
      <defs>
        <linearGradient id="ornamentTone" x1="0" y1="0" x2="0" y2="1">
          <stop offset="0" stop-color="#b00a0c"/>
          <stop offset="0.5" stop-color="#7a0607"/>
          <stop offset="1" stop-color="#b00a0c"/>
        </linearGradient>
      </defs>
      <rect class="ornament-fill" x="22" y="150" width="53" height="490" role="img" aria-label="Scrolling swirl border pattern"/>
      <rect class="ornament-fill" x="375" y="150" width="53" height="490" role="img" aria-label="Scrolling swirl border pattern"/>
      <rect class="ornament-fill" x="150" y="22" width="150" height="60" role="img" aria-label="Swirl border pattern"/>
      <rect class="ornament-fill" x="150" y="708" width="150" height="60" role="img" aria-label="Swirl border pattern"/>
      <rect class="ornament-fill" x="75" y="82" width="300" height="626" role="img" aria-label="Scrollwork filling around the central medallion"/>
      <polygon class="ornament-solid" points="225,80 375,395 225,710 75,395" role="img" aria-label="Symmetrical tribal medallion ornament"/>
      <rect class="frame-line" x="0" y="145" width="450" height="14"/>
      <rect class="frame-line" x="0" y="631" width="450" height="14"/>
      <circle class="corner-arc" cx="0" cy="0" r="150"/>
      <circle class="corner-arc" cx="450" cy="0" r="150"/>
      <circle class="corner-arc" cx="0" cy="790" r="150"/>
      <circle class="corner-arc" cx="450" cy="790" r="150"/>
      <circle class="corner-ring" cx="60" cy="60" r="37"/>
      <circle class="corner-ring" cx="392" cy="60" r="37"/>
      <circle class="corner-ring" cx="57" cy="730" r="37"/>
      <circle class="corner-ring" cx="392" cy="732" r="37"/>
      <circle class="corner-emblem" cx="60" cy="60" r="15" role="img" aria-label="Small flourish emblem"/>
      <circle class="corner-emblem" cx="392" cy="60" r="15" role="img" aria-label="Small flourish emblem"/>
      <circle class="corner-emblem" cx="57" cy="730" r="15" role="img" aria-label="Small flourish emblem"/>
      <circle class="corner-emblem" cx="392" cy="732" r="15" role="img" aria-label="Small flourish emblem"/>
    </svg>
  </div>

  <!-- Identity side -->
  <div class="card card--identity">
    <svg viewBox="0 0 450 790" xmlns="http://www.w3.org/2000/svg">
      <rect class="ornament-fill" x="22" y="150" width="50" height="490" role="img" aria-label="Scrolling swirl border pattern"/>
      <rect class="ornament-fill" x="378" y="150" width="50" height="490" role="img" aria-label="Scrolling swirl border pattern"/>
      <rect class="ornament-fill" x="150" y="22" width="150" height="52" role="img" aria-label="Swirl border pattern"/>
      <rect class="ornament-fill" x="150" y="716" width="150" height="52" role="img" aria-label="Swirl border pattern"/>
      <rect class="frame-line" x="72" y="150" width="7" height="490"/>
      <rect class="frame-line" x="371" y="150" width="7" height="490"/>
      <rect class="frame-line" x="0" y="145" width="450" height="14"/>
      <rect class="frame-line" x="0" y="631" width="450" height="14"/>
      <circle class="corner-arc" cx="0" cy="0" r="150"/>
      <circle class="corner-arc" cx="450" cy="0" r="150"/>
      <circle class="corner-arc" cx="0" cy="790" r="150"/>
      <circle class="corner-arc" cx="450" cy="790" r="150"/>
      <circle class="corner-ring" cx="60" cy="60" r="37"/>
      <circle class="corner-ring" cx="392" cy="60" r="37"/>
      <circle class="corner-ring" cx="57" cy="730" r="37"/>
      <circle class="corner-ring" cx="392" cy="732" r="37"/>
      <circle class="corner-emblem" cx="60" cy="60" r="15" role="img" aria-label="Small flourish emblem"/>
      <circle class="corner-emblem" cx="392" cy="60" r="15" role="img" aria-label="Small flourish emblem"/>
      <circle class="corner-emblem" cx="57" cy="730" r="15" role="img" aria-label="Small flourish emblem"/>
      <circle class="corner-emblem" cx="392" cy="732" r="15" role="img" aria-label="Small flourish emblem"/>
      <path class="ornament-solid" d="M225,85 C300,150 357,220 350,270 C340,315 280,320 225,290 C170,320 110,315 100,270 C93,220 150,150 225,85 Z" role="img" aria-label="Flourish ornament with swirls and dots"/>
      <path class="ornament-solid" d="M225,700 C300,635 357,565 350,515 C340,470 280,465 225,495 C170,465 110,470 100,515 C93,565 150,635 225,700 Z" role="img" aria-label="Flourish ornament with swirls and dots"/>
      <text class="card-name" x="225" y="385" text-anchor="middle" textLength="270" lengthAdjust="spacingAndGlyphs">Desmond Halloway</text>
      <text class="card-site" x="225" y="440" text-anchor="middle" textLength="270" lengthAdjust="spacingAndGlyphs">www.TrickvaleShows.com</text>
    </svg>
  </div>

</div>
</body>
</html>
```